Tuition Center Website

We need a new web site for a tutoring company based in sydney.

We only teach senior highschool students and pride ourselves on building the students abilities to think their way through life.

I would like a bright and vibrant website that looks professional and modern.
It needs to look simple and neat but also have the functionality we need.
Images and flash would be good.

Please keep in mind that the site must be appealing to a younger audience.

We need a multipage website with the following navigation bars:

1.Home (As logo not "home" button)
I would like a news box/ticker somewhere that can stream our chatterbook and peeplr feeds and also any news updates we want to put up.
Subscribe to newsletter button.

2. About us.
This needs to be a pull down into:
-What we do
-Why we do it
-How we do it

3. Courses
Pulldown into:
-Maths
-English
-Science
(we may need to attach extra pages behind these e.g. Courses/Science/Physics or Courses/Science/Chemistry and possibly add a link to a new formvik form)

4. Inspired
This page is like a blog page where we can upload videos, links to articles that we find to be inspiring and hopefully will inspire others.

5. Inspire
This is a recruitment page. Only content here.

6. Contact us.
Trovix map widget and a 'contact us' form

* Our branding requires green close to #12FF3D

***Please have a look at the current website.
@ www.velmoralearning.com.au

Thanks everybody hope the revision of my brief is better and more informative than my last one
Updates

Target Market(s)

senior highschool students aged 15-19, parents ( to a lesser degree)

Industry/Entity Type

It Company

Requirements
Must have
• Ability to change content on pages.

The green doesn't have to be everywhere, but it must be obvious that it is our colour.

Nice to have
• Sites with a nicer mix of images and flash will be given more consideration. But then again, if you amaze us, you amaze us and we will go with your design.
Should not have
• Should stay away from ocre, brown colours and serif fonts.

```html
<!DOCTYPE html>
<html lang="en">
<head>
<meta charset="utf-8">
<title>Velmora Learning | HSC tutoring &amp; mentoring</title>
<link href="https://fonts.googleapis.com/css2?family=Open+Sans:wght@400;600;700&family=Gochi+Hand&display=swap" rel="stylesheet">
<style>
:root{
  --green:#3dc21b;
  --green-dark:#2f9e12;
  --green-bright:#12ff3d;
  --ink:#222;
  --text:#555;
  --grey-band:#e6e6e6;
  --dark:#2b2b2b;
  --darker:#1e1e1e;
  --nav:#3a3a3a;
  --white:#fff;
}
*{box-sizing:border-box;margin:0;padding:0}
html,body{width:889px;height:1200px;overflow:hidden}
body{font-family:"Open Sans",Arial,sans-serif;color:var(--text);background:var(--white);font-size:10px;line-height:1.5}
.wrap{width:666px;margin:0 auto;position:relative}
a{color:var(--green-dark);text-decoration:none}

/* header */
.site-header{height:89px}
.site-header .wrap{height:89px;display:flex;align-items:center;justify-content:space-between}
.brand{display:flex;align-items:center;gap:8px;font-size:22px;font-weight:700;color:var(--ink)}
.brand-mark{width:30px;height:30px;background:var(--green)}
.header-contact{text-align:right;font-size:9.5px;color:var(--ink);line-height:1.6}
.social{display:flex;gap:4px;justify-content:flex-end;margin-top:3px}
.social span{width:14px;height:14px;border-radius:50%;background:#777;display:block}

/* nav */
.main-nav{background:var(--nav);height:24px}
.main-nav ul{list-style:none;display:flex;height:24px;align-items:center}
.main-nav li{color:var(--white);font-size:10px;padding:0 16px;line-height:24px}
.main-nav li.active{background:var(--green)}

/* hero */
.hero{background:var(--green);height:217px}
.hero .wrap{height:217px}
.trial{position:absolute;left:53px;top:20px;width:281px;height:177px;border:2px solid var(--white);text-align:center;color:var(--white)}
.trial h2{background:var(--white);color:var(--ink);font-family:"Gochi Hand",cursive;font-weight:400;font-size:26px;line-height:1.05;padding:10px 0 8px;margin:10px 18px 0}
.trial p{font-size:9px;padding:8px 24px 0;line-height:1.45}
.trial .btn{display:inline-block;margin-top:10px;background:var(--darker);color:var(--white);font-weight:700;font-size:10px;padding:6px 18px}
.mottos{position:absolute;left:392px;top:34px;list-style:none}
.mottos li{display:flex;align-items:center;gap:12px;font-family:"Gochi Hand",cursive;color:var(--white);font-size:23px;line-height:50px;white-space:nowrap}
.mottos .ico{width:32px;height:32px;border-radius:4px;background:rgba(255,255,255,.28);flex:none}

/* intro */
.intro{height:218px}
.intro .wrap{padding-top:40px}
.intro h1{font-size:19px;color:var(--ink);font-weight:700}
.intro p{width:440px;font-size:9.5px;margin-top:8px}
.intro .more{display:block;margin-top:14px;font-size:9.5px}
.intro .art{position:absolute;right:10px;top:30px;width:160px;height:150px;background:linear-gradient(#f4f4f4,#e2efe0)}

/* beliefs */
.beliefs{background:var(--grey-band);height:227px}
.beliefs .wrap{height:227px;display:flex;padding-top:20px}
.belief{width:165px;margin-right:12px}
.belief h3{font-family:"Gochi Hand",cursive;font-weight:400;font-size:16px;color:var(--green-dark);margin-bottom:10px;white-space:nowrap}
.belief ul{list-style:none}
.belief li{display:flex;gap:6px;align-items:center;font-size:9.5px;color:var(--ink);margin-bottom:6px}
.belief li svg{flex:none}
.news{margin-left:auto;width:230px;height:200px;background:var(--dark);margin-top:-8px;padding:14px 16px;color:var(--white)}
.news h3{font-family:"Gochi Hand",cursive;font-weight:400;font-size:19px;margin-bottom:6px}
.news ul{list-style:none}
.news li{display:flex;gap:7px;align-items:center;font-size:9.5px;line-height:21px}
.news li::before{content:"";width:8px;height:8px;background:var(--green);flex:none}

/* testimonials */
.testimonials{height:261px}
.testimonials .wrap{padding-top:14px}
.testimonials h2{font-size:18px;color:var(--ink);font-weight:700;margin-bottom:12px}
.quote{width:430px;font-size:9px;margin-bottom:12px}
.quote cite{display:block;font-style:normal;color:var(--green-dark);margin-top:8px}
.view-all{font-size:9.5px}
.feed{position:absolute;right:0;top:44px;width:200px;height:150px;border:1px solid #ccc;padding:8px;font-size:8.5px}
.feed-head{display:flex;gap:6px;align-items:center;border-bottom:1px solid #ddd;padding-bottom:6px;color:var(--ink);font-weight:600}
.feed-head span{width:24px;height:24px;background:var(--green)}
.feed p{margin-top:6px;line-height:1.4}

/* footer */
.site-footer{background:var(--dark);height:134px;color:#ccc}
.site-footer .wrap{height:134px;padding-top:14px;display:flex}
.sitemap h4{color:var(--white);font-size:12px;margin-bottom:6px}
.sitemap ul{list-style:none;font-size:9.5px;line-height:1.7}
.map{margin-left:auto;width:150px;height:90px;background:linear-gradient(135deg,#d9d6cc,#c6d8b8);margin-top:8px}
.contact{width:170px;margin-left:14px;margin-top:8px;list-style:none;font-size:8.5px;line-height:1.5}
.contact li{display:flex;gap:6px;margin-bottom:4px}
.contact li::before{content:"";width:7px;height:7px;margin-top:3px;background:var(--green);flex:none}
.bottom-bar{background:var(--darker);height:30px;color:#aaa;font-size:9px}
.bottom-bar .wrap{height:30px;display:flex;align-items:center;justify-content:space-between}
.follow{display:flex;align-items:center;gap:5px}
.follow span{width:14px;height:14px;border-radius:50%;background:#666}
</style>
</head>
<body>
<header class="site-header">
  <div class="wrap">
    <div class="brand"><span class="brand-mark"></span>Velmora Learning</div>
    <div class="header-contact">
      Phone: (02) 5550 1457<br>Email: learn@velmoralearning.com.au
      <div class="social"><span aria-label="chatterbook"></span><span aria-label="peeplr"></span><span aria-label="video"></span></div>
    </div>
  </div>
</header>

<nav class="main-nav">
  <ul class="wrap">
    <li class="active">Home</li><li>About us</li><li>Courses</li><li>Inspired</li><li>Contact Us</li>
  </ul>
</nav>

<section class="hero">
  <div class="wrap">
    <div class="trial">
      <h2>Ask For Your<br>Free Trial Lesson</h2>
      <p>Because we believe you shouldn't have to sign up until you see what it's actually like. Call or email us now!</p>
      <span class="btn">Send an Enquiry</span>
    </div>
    <ul class="mottos">
      <li><span class="ico" role="img" aria-label="Drawn lightbulb icon"></span>Inspiring Minds</li>
      <li><span class="ico" role="img" aria-label="Drawn seedling icon"></span>Nurturing Potential</li>
      <li><span class="ico" role="img" aria-label="Drawn toolbox icon"></span>Equipping Success</li>
    </ul>
  </div>
</section>

<section class="intro">
  <div class="wrap">
    <h1>Real HSC coaching &amp; mentoring.</h1>
    <p>The HSC help you need, in the years you need it. We offer small classes, individualised attention and genuine care for each student. It's different - in a good way. Feel free to find out more about us, and let us know if there's any way we can help you on your journey.</p>
    <a class="more" href="#">Read More</a>
    <div class="art" role="img" aria-label="Sketch of a graduate with books and a diploma"></div>
  </div>
</section>

<section class="beliefs">
  <div class="wrap">
    <div class="belief">
      <h3>We Don't Believe In:</h3>
      <ul>
        <li><svg width="9" height="9" viewBox="0 0 9 9"><path d="M1 1l7 7M8 1L1 8" stroke="#c33" stroke-width="2"/></svg>Massive classes;</li>
        <li><svg width="9" height="9" viewBox="0 0 9 9"><path d="M1 1l7 7M8 1L1 8" stroke="#c33" stroke-width="2"/></svg>Spoon-feeding answers;</li>
        <li><svg width="9" height="9" viewBox="0 0 9 9"><path d="M1 1l7 7M8 1L1 8" stroke="#c33" stroke-width="2"/></svg>One-size-fits-all teaching.</li>
      </ul>
    </div>
    <div class="belief">
      <h3>We Do Believe In:</h3>
      <ul>
        <li><svg width="10" height="9" viewBox="0 0 10 9"><path d="M1 5l3 3 5-7" stroke="#2f9e12" stroke-width="2" fill="none"/></svg>Small classes tailored to you;</li>
        <li><svg width="10" height="9" viewBox="0 0 10 9"><path d="M1 5l3 3 5-7" stroke="#2f9e12" stroke-width="2" fill="none"/></svg>Helping you think for yourself;</li>
        <li><svg width="10" height="9" viewBox="0 0 10 9"><path d="M1 5l3 3 5-7" stroke="#2f9e12" stroke-width="2" fill="none"/></svg>Genuinely caring about who you are as an individual.</li>
      </ul>
    </div>
    <aside class="news">
      <h3>Recent News</h3>
      <ul>
        <li>Year 11 FREE HSC Workshops!</li>
        <li>Uni Open Days 2012</li>
        <li>Considering Studying Interstate?</li>
        <li>Year 11 FREE HSC Workshops!</li>
        <li>Considering Studying Interstate?</li>
        <li>Uni Open Days 2012</li>
      </ul>
    </aside>
  </div>
</section>

<section class="testimonials">
  <div class="wrap">
    <h2>What Our Students Say</h2>
    <blockquote class="quote">I like the support the most, how the people and teachers here pick you off your feet, make you do better and tell you that it's not the end of the world!<cite>- Marissa, Ashvale NSW HSC</cite></blockquote>
    <blockquote class="quote">I like the support the most, how the people and teachers here pick you off your feet, make you do better and tell you that it's not the end of the world!<cite>- Marissa, Ashvale NSW HSC</cite></blockquote>
    <a class="view-all" href="#">View All</a>
    <div class="feed">
      <div class="feed-head"><span></span>Velmora Learning on chatterbook</div>
      <p>We are thrilled to share that our Year 12 students have done amazingly well this term. Keep up the great work and remember we are here to help every step of the way!</p>
    </div>
  </div>
</section>

<footer class="site-footer">
  <div class="wrap">
    <div class="sitemap">
      <h4>Site Map</h4>
      <ul><li>Home</li><li>About us</li><li>Courses</li><li>Inspired</li><li>Contact Us</li></ul>
    </div>
    <div class="map" role="img" aria-label="Trovix map showing the tutoring centre location"></div>
    <ul class="contact">
      <li>Street: 12 Larkin St, Ashvale NSW 2199</li>
      <li>Phone: (02) 5550 1457</li>
      <li>Email: learn@velmoralearning.com.au</li>
    </ul>
  </div>
</footer>
<div class="bottom-bar">
  <div class="wrap">
    <span>© 2013 Velmora Learning | HSC tutoring &amp; mentoring</span>
    <span class="follow">Follow us <span aria-label="chatterbook"></span><span aria-label="peeplr"></span></span>
  </div>
</div>
</body>
</html>
```